Pathways to Brightmoor Land Ventures

size of the ad - 8”x 10.75" plus 0.25" bleed
I would like an ad for a magazine that will stand out and make people want to read the ad.
The ad should not be crowded and people reading the ad will be able to read the text.
I would like it to be a creative and modern-day design.
the list of topics should not be the focus of the ad.
the text is attached.
If you decide to use people in the ad then please no ladies.
please note that leave over 1 inch for the bottom of the footer

```html
<!DOCTYPE html>
<html lang="en">
<head>
<meta charset="utf-8">
<title>Real Estate Course — Pathways to Brightmoor Land Ventures</title>
<link rel="stylesheet" href="https://fonts.googleapis.com/css2?family=Bebas+Neue&family=Barlow+Condensed:wght@400;600&family=Barlow:wght@400&display=swap">
<style>
  :root {
    --ink-dark: #0c0d10;
    --photo-red-top: #c53b36;
    --photo-red-mid: #7a2422;
    --photo-red-low: #2a0f0f;
    --photo-dark-top: #2b2f36;
    --photo-dark-low: #050607;
    --accent-blue: #1f74c6;
    --text-white: #ffffff;
    --text-grey: #d8d9dc;
    --rule: rgba(255,255,255,0.35);
  }
  * { margin: 0; padding: 0; box-sizing: border-box; }
  html, body { width: 928px; height: 1200px; overflow: hidden; background: var(--ink-dark); }
  .ad { position: relative; width: 928px; height: 1200px; overflow: hidden; }
  .backdrop { position: absolute; inset: 0; width: 928px; height: 1200px; }

  .copy { position: absolute; right: 77px; text-align: right; color: var(--text-white); }
  .title {
    top: 76px; font-family: "Bebas Neue", sans-serif; font-size: 100px; line-height: 77px;
    color: var(--accent-blue); letter-spacing: 0;
  }
  .subtitle {
    top: 336px; font-family: "Barlow Condensed", sans-serif; font-weight: 600;
    font-size: 30px; line-height: 35px; text-transform: uppercase;
  }
  .slogan {
    top: 481px; font-family: "Barlow Condensed", sans-serif; font-weight: 400;
    font-size: 28px; line-height: 29px; text-transform: uppercase;
  }
  .rule { position: absolute; left: 574px; width: 281px; height: 1px; background: var(--rule); }
  .section-head {
    font-family: "Barlow Condensed", sans-serif; font-weight: 400; font-size: 32px;
    line-height: 34px; color: var(--accent-blue); text-transform: uppercase;
  }
  .details {
    font-family: "Barlow Condensed", sans-serif; font-weight: 400; font-size: 18px;
    line-height: 21px; text-transform: uppercase;
  }
  .location { top: 612px; }
  .location .details { margin-top: 8px; }
  .early-bird { top: 772px; }
  .early-bird .details { margin-top: 6px; line-height: 18px; }
  .topics { top: 898px; }
  .topic-list { list-style: none; margin-top: 14px; }
  .topic-list li {
    font-family: "Barlow", sans-serif; font-size: 15px; line-height: 18.2px;
    color: var(--text-grey); text-transform: uppercase; padding-right: 11px; position: relative;
  }
  .topic-list li::after {
    content: ""; position: absolute; right: 0; top: 7px; width: 4px; height: 4px; background: var(--text-grey);
  }
</style>
</head>
<body>
<main class="ad">
  <svg class="backdrop" viewBox="0 0 928 1200" role="img" aria-label="Photograph of a modern two-storey house with wood siding at dusk, left half tinted red, right half in dark shadow">
    <defs>
      <linearGradient id="redTint" x1="0" y1="0" x2="0.2" y2="1">
        <stop offset="0" stop-color="var(--photo-red-top)"/>
        <stop offset="0.5" stop-color="var(--photo-red-mid)"/>
        <stop offset="1" stop-color="var(--photo-red-low)"/>
      </linearGradient>
      <linearGradient id="darkTint" x1="0" y1="0" x2="0" y2="1">
        <stop offset="0" stop-color="var(--photo-dark-top)"/>
        <stop offset="0.6" stop-color="#15171b"/>
        <stop offset="1" stop-color="var(--photo-dark-low)"/>
      </linearGradient>
    </defs>
    <rect x="0" y="0" width="928" height="1200" fill="url(#redTint)"/>
    <polygon points="516,0 928,0 928,1200 516,1200 516,473 430,265 516,58" fill="url(#darkTint)"/>
    <polyline points="486,0 486,58 385,265 486,473 486,1200" fill="none" stroke="rgba(255,255,255,0.55)" stroke-width="7"/>
  </svg>

  <h1 class="copy title">Real<br>Estate<br>Course</h1>
  <h2 class="copy subtitle">Pathways to<br>Brightmoor Land<br>Ventures</h2>
  <div class="rule" style="top:462px"></div>
  <p class="copy slogan">Investing in knowledge is<br>investing in opportunities.</p>
  <div class="rule" style="top:578px"></div>

  <section class="copy location">
    <h3 class="section-head">Alderbrook</h3>
    <p class="details">10 -Tuesday evenings sessions<br>Starting Feb.28<br>Limited partial scholarships</p>
  </section>
  <div class="rule" style="top:744px"></div>

  <section class="copy early-bird">
    <h3 class="section-head">Early Bird Special</h3>
    <p class="details">For those that started or would<br>like to go into real estate</p>
  </section>
  <div class="rule" style="top:876px"></div>

  <section class="copy topics">
    <h3 class="section-head">Topics: Partial Listing</h3>
    <ul class="topic-list">
      <li>Real estate investment strategies</li>
      <li>Due diligence</li>
      <li>Financing</li>
      <li>Underwriting</li>
      <li>Property management</li>
      <li>Real estate legal basics</li>
      <li>Sourcing deals</li>
      <li>Syndication</li>
      <li>Dealing with brokers</li>
      <li>Tax fundamentals</li>
    </ul>
  </section>
</main>
</body>
</html>
```